we are a college and require a design of a printable graduation certificate

our courses range from certicate III to Diploma

We would a high quality design, similar to a unveristy degree, so its meaning full to the students and looks great on the wall

our college website is: www.marlowinstitute.example.au

College

• security feature like water mark or stamp

```html
<!DOCTYPE html>
<html lang="en">
<head>
<meta charset="utf-8">
<title>Marlow Institute – Certificate of Graduation</title>
<link href="https://fonts.googleapis.com/css2?family=Didact+Gothic&family=Kaushan+Script&display=swap" rel="stylesheet">
<style>
  :root {
    --frame-black: #000000;
    --paper: #ffffff;
    --ink: #3a3a3a;
    --ink-soft: #4a4a4a;
    --band-blue: #12a6dc;
    --swoosh-grey: #c4c6c8;
    --illustration-grey: #e6e6e6;
    --seal-red: #b3161c;
  }
  html, body {
    margin: 0;
    padding: 0;
    overflow: hidden;
    background: var(--frame-black);
  }
  .certificate {
    position: relative;
    width: 1200px;
    height: 855px;
    overflow: hidden;
    background: var(--frame-black);
    font-family: "Didact Gothic", sans-serif;
    color: var(--ink);
  }
  .certificate__art {
    position: absolute;
    inset: 0;
  }
  .text {
    position: absolute;
    margin: 0;
    line-height: 1;
    white-space: nowrap;
  }
  .college-name {
    left: 161px;
    top: 312px;
    font-size: 36px;
    letter-spacing: 0.5px;
    color: var(--ink);
  }
  .title {
    left: 129px;
    top: 404px;
    font-family: "Kaushan Script", cursive;
    font-size: 46px;
    letter-spacing: 2px;
    color: var(--ink);
  }
  .field-label {
    font-size: 29px;
    color: var(--ink-soft);
  }
  .field-label--certify { left: 127px; top: 499px; }
  .field-label--course  { left: 127px; top: 575px; }
  .field-label--on      { left: 127px; top: 644px; }
  .sign-label {
    font-size: 22px;
    color: var(--ink-soft);
  }
  .sign-label--name      { left: 126px; top: 703px; }
  .sign-label--signature { left: 126px; top: 743px; }
  .sign-label--date      { left: 483px; top: 743px; }
</style>
</head>
<body>
<main class="certificate">
  <svg class="certificate__art" width="1200" height="855" viewBox="0 0 1200 855" aria-hidden="false">
    <defs>
      <radialGradient id="halftone-tone" cx="0.5" cy="0.5" r="0.5">
        <stop offset="0" stop-color="#e9e9e9"/>
        <stop offset="1" stop-color="#ffffff" stop-opacity="0"/>
      </radialGradient>
      <linearGradient id="cap-tone" x1="0" y1="0" x2="1" y2="1">
        <stop offset="0" stop-color="#f1ece4"/>
        <stop offset="1" stop-color="var(--illustration-grey)"/>
      </linearGradient>
    </defs>

    <!-- paper -->
    <rect class="paper" x="69" y="47" width="1058" height="746" fill="var(--paper)"/>

    <!-- faint background pattern area -->
    <g role="img" aria-label="Faint grey halftone dot pattern sweeping across the certificate background">
      <ellipse cx="430" cy="600" rx="520" ry="260" fill="url(#halftone-tone)"/>
    </g>

    <!-- graduation cap and scroll illustration area -->
    <g role="img" aria-label="Faded illustration of a graduation cap with tassel and a rolled diploma scroll">
      <rect x="660" y="130" width="333" height="224" rx="40" fill="url(#cap-tone)" opacity="0.7"/>
    </g>

    <!-- grey swoosh -->
    <path class="swoosh" d="M690,793 C900,700 1078,560 1070,337 C1096,520 1015,705 880,793 Z" fill="var(--swoosh-grey)"/>

    <!-- blue corner band -->
    <path class="band" d="M915,47 C1015,85 1100,225 1100,414 C1100,600 1010,735 906,793 L1127,793 L1127,47 Z" fill="var(--band-blue)"/>

    <!-- inner frame line -->
    <rect class="frame-line" x="76" y="53" width="1044" height="734" fill="none" stroke="var(--frame-black)" stroke-width="2.5"/>

    <!-- form rules -->
    <g class="rules" stroke="var(--ink-soft)" stroke-width="1.2">
      <line x1="417" y1="522" x2="909" y2="522"/>
      <line x1="608" y1="598" x2="909" y2="598"/>
      <line x1="192" y1="664" x2="906" y2="664"/>
    </g>
    <g class="dotted-rules" stroke="var(--ink-soft)" stroke-width="2" stroke-dasharray="2 3">
      <line x1="207" y1="719" x2="408" y2="719"/>
      <line x1="246" y1="761" x2="450" y2="761"/>
      <line x1="550" y1="761" x2="754" y2="761"/>
    </g>

    <!-- seal -->
    <circle class="seal" cx="1057" cy="673" r="42" fill="var(--seal-red)"/>
  </svg>

  <p class="text college-name">MARLOW INSTITUTE</p>
  <h1 class="text title">Certificate of Graduation</h1>

  <p class="text field-label field-label--certify">This is to Certify that</p>
  <p class="text field-label field-label--course">has Completed a&nbsp; course of study in</p>
  <p class="text field-label field-label--on">On</p>

  <p class="text sign-label sign-label--name">Name</p>
  <p class="text sign-label sign-label--signature">Signature</p>
  <p class="text sign-label sign-label--date">Date</p>
</main>
</body>
</html>
```